Visitenkarten-Design für Autowerkstatt/-verwertung
Zielgruppe
Unser Unternehmen besteht aus zwei Bereiche:
- Autoverwertung
- Autowerkstatt
Aufgabenstellung
Informationen auf der Visitenkarte:
'Brunnhofer' - Logo
Lindenauer Str. 31
80993 München
Autoverwertung Autoteile
www.autoverwertung-brunnhofer-beispiel.de
info@autoverwertung-brunnhofer-beispiel.de
Autowerkstatt
www.auto-brunnhofer-beispiel.de
info@auto-brunnhofer-beispiel.de
Öffnungszeiten:
Mo-Fr
08.00 - 12.00 Uhr und 13.00 - 17.00 Uhr
Farblich sollte die Visitenkarte sich an das Logo anpassen. Visitenkarte 2-4 seitig.

```html
<!DOCTYPE html>
<html lang="de">
<head>
<meta charset="utf-8">
<title>Brunnhofer – Visitenkarte</title>
<link rel="stylesheet" href="https://fonts.googleapis.com/css2?family=Nunito:wght@600;700;800&family=Gochi+Hand&display=swap">
<style>
  :root {
    --bg: #eeeeee;
    --card: #ffffff;
    --border: #8a8a8a;
    --fold: #c9c9c9;
    --red: #d3121a;
    --ink: #2b2b2b;
    --grey: #3a3a3a;
    --map-light: #f4f4f4;
    --map-mid: #dedede;
    --decor-red: #efb9ba;
    --decor-grey: #cfcfcf;
  }
  * { box-sizing: border-box; margin: 0; padding: 0; }
  html, body { width: 750px; height: 1200px; overflow: hidden; }
  body {
    background: var(--bg);
    font-family: "Nunito", sans-serif;
    color: var(--ink);
    position: relative;
  }
  .spread {
    position: absolute;
    left: 15px;
    width: 720px;
    height: 230px;
    background: var(--card);
    border: 1px solid var(--border);
    display: flex;
  }
  .spread--outside { top: 345px; }
  .spread--inside { top: 625px; }
  .panel { position: relative; width: 50%; height: 100%; overflow: hidden; }
  .panel + .panel { border-left: 1px solid var(--fold); }

  /* Outside left: location map */
  .map-area {
    position: absolute; inset: 0;
    background: radial-gradient(circle at 60% 45%, var(--map-light), var(--map-mid));
  }
  .address-bubble {
    position: absolute; left: 31px; top: 41px;
    width: 124px; height: 124px; border-radius: 50%;
    background: var(--card); border: 1.5px solid var(--grey);
    display: flex; align-items: center; justify-content: center; gap: 6px;
  }
  .address-bubble .pin { width: 12px; height: 12px; border-radius: 50%; background: var(--red); flex: none; }
  .address { font-size: 10.5px; font-weight: 700; line-height: 1.3; color: var(--ink); }
  .address .zip { color: var(--red); }

  /* Outside right: brand */
  .brand { position: absolute; left: 18px; top: 62px; width: 320px; }
  .brand-name { display: flex; align-items: center; gap: 10px; }
  .brand-name .dot { width: 30px; height: 30px; border-radius: 50%; background: var(--red); }
  .brand-name span { font-size: 34px; font-weight: 800; color: var(--grey); line-height: 1; }
  .brand-rule { margin-top: 6px; height: 3px; background: var(--red); }
  .brand-tagline { margin-top: 3px; font-size: 10.5px; font-weight: 800; color: var(--red); word-spacing: 2px; white-space: nowrap; }
  .hours {
    position: absolute; right: 22px; top: 128px;
    font-family: "Gochi Hand", cursive; font-size: 14px; line-height: 1.25;
    text-align: center; color: var(--ink); transform: rotate(-8deg);
  }
  .hours .days { text-decoration: underline; }

  /* Inside left: decoration */
  .decor {
    position: absolute; left: -70px; top: -40px;
    width: 260px; height: 260px; border-radius: 50%;
    background: radial-gradient(circle, var(--decor-grey) 0 45%, var(--decor-red) 46% 100%);
    opacity: 0.55;
  }

  /* Inside right: contacts */
  .contacts { position: absolute; left: 54px; top: 34px; }
  .contact-group + .contact-group { margin-top: 20px; }
  .contact-group h2 {
    font-size: 11px; font-weight: 800; color: var(--red);
    text-decoration: underline; margin-bottom: 6px;
  }
  .contact-group ul { list-style: none; }
  .contact-group li { display: flex; align-items: center; gap: 8px; font-size: 11px; font-weight: 700; line-height: 1.45; }
  .contact-group li.phone { margin-top: 5px; }
  .icon { width: 11px; height: 11px; flex: none; }
</style>
</head>
<body>

<section class="spread spread--outside">
  <div class="panel panel--map">
    <div class="map-area" role="img" aria-label="Stadtplan von München mit markiertem Standort der Werkstatt"></div>
    <div class="address-bubble">
      <span class="pin"></span>
      <p class="address">Lindenauer Str. 31<br><span class="zip">80993</span> München</p>
    </div>
  </div>
  <div class="panel panel--brand">
    <div class="brand">
      <div class="brand-name"><span class="dot"></span><span>Brunnhofer</span></div>
      <div class="brand-rule"></div>
      <p class="brand-tagline">Autoverwertung Autoteile Autohandel Autowerkstatt</p>
    </div>
    <p class="hours"><span class="days">Mo-Fr</span><br>08.00 - 12.00 Uhr<br>—<br>13.00 - 17.00 Uhr</p>
  </div>
</section>

<section class="spread spread--inside">
  <div class="panel panel--decor">
    <div class="decor" role="img" aria-label="Dezentes Werkstatt-Dekor in Rot und Grau"></div>
  </div>
  <div class="panel panel--contacts">
    <div class="contacts">
      <div class="contact-group">
        <h2>Autoverwertung Autoteile</h2>
        <ul>
          <li><svg class="icon" viewBox="0 0 12 12"><circle cx="6" cy="6" r="5" fill="none" stroke="#2b2b2b" stroke-width="1.2"/><ellipse cx="6" cy="6" rx="2.2" ry="5" fill="none" stroke="#2b2b2b" stroke-width="1"/><line x1="1" y1="6" x2="11" y2="6" stroke="#2b2b2b" stroke-width="1"/></svg>www.autoverwertung-brunnhofer-beispiel.de</li>
          <li><svg class="icon" viewBox="0 0 12 12"><rect x="0.5" y="2.5" width="11" height="7" fill="none" stroke="#2b2b2b" stroke-width="1.2"/><polyline points="0.5,2.5 6,7 11.5,2.5" fill="none" stroke="#2b2b2b" stroke-width="1.2"/></svg>info@autoverwertung-brunnhofer-beispiel.de</li>
          <li class="phone"><svg class="icon" viewBox="0 0 12 12"><path d="M2.5 1 L4.5 1 L5.3 3.6 L4 4.6 Q5 7 7.4 8 L8.4 6.7 L11 7.5 L11 9.5 Q10.5 11 9 11 Q1 10 1 3 Q1 1.5 2.5 1 Z" fill="#2b2b2b"/></svg>089 - 41 28 60 17</li>
        </ul>
      </div>
      <div class="contact-group">
        <h2>Autowerkstatt</h2>
        <ul>
          <li><svg class="icon" viewBox="0 0 12 12"><circle cx="6" cy="6" r="5" fill="none" stroke="#2b2b2b" stroke-width="1.2"/><ellipse cx="6" cy="6" rx="2.2" ry="5" fill="none" stroke="#2b2b2b" stroke-width="1"/><line x1="1" y1="6" x2="11" y2="6" stroke="#2b2b2b" stroke-width="1"/></svg>www.auto-brunnhofer-beispiel.de</li>
          <li><svg class="icon" viewBox="0 0 12 12"><rect x="0.5" y="2.5" width="11" height="7" fill="none" stroke="#2b2b2b" stroke-width="1.2"/><polyline points="0.5,2.5 6,7 11.5,2.5" fill="none" stroke="#2b2b2b" stroke-width="1.2"/></svg>info@auto-brunnhofer-beispiel.de</li>
          <li class="phone"><svg class="icon" viewBox="0 0 12 12"><path d="M2.5 1 L4.5 1 L5.3 3.6 L4 4.6 Q5 7 7.4 8 L8.4 6.7 L11 7.5 L11 9.5 Q10.5 11 9 11 Q1 10 1 3 Q1 1.5 2.5 1 Z" fill="#2b2b2b"/></svg>0160 - 52 74 38 9</li>
        </ul>
      </div>
    </div>
  </div>
</section>

</body>
</html>
```